New brand of Beef Tallow. Label & carton design for BBQ enthusiasts

We currently have a PET tub that will be clear, and a solid black lid. It will be 500gm in net weight and be used to store beef tallow. The brand will be under the Telby Preserving Co brand, and this has an existing logo. We want the ultimate design to be informed by some niche brands that operate in the BBQ and condiments categories. I also need a carton design for the beef tallow- two colour max. ***Note that the label dieline is upside down!

Target Market(s)

BBQ Enthusiasts

Industry/Entity Type

Food, Consumer Goods

Requirements
Must have
• Telby Preserving logo, all of the required labelling, Nutrition Information Panel (to be supplied), barcode, product attributes, a top of lid and wrap around label. Use of terminology such as 'Suet, Tallow, Beef Fat' which are the key indicators of the product. I also want it to reference that it is made in Papua New Guinea.

```html
<!DOCTYPE html>
<html lang="en">
<head>
<meta charset="utf-8">
<title>Telby Preserving Co – Beef Tallow Label</title>
<link href="https://fonts.googleapis.com/css2?family=Josefin+Sans:ital,wght@0,300;0,400;0,600;1,300&family=Nunito:ital,wght@0,900;1,900&family=Oswald:wght@500&display=swap" rel="stylesheet">
<style>
  :root {
    --peach: #e5a888;
    --peach-deep: #df9b79;
    --peach-pale: #f6e5db;
    --ink: #111111;
    --paper: #ffffff;
    --guide: #9fb3d9;
    --label-grey: #a9a9a9;
    --muted: #6e5245;
  }
  html, body { margin: 0; padding: 0; overflow: hidden; background: var(--paper); }
  .artboard { display: block; width: 1200px; height: 665px; }
  .side-tag { font-family: Arial, Helvetica, sans-serif; font-size: 22px; fill: var(--label-grey); }
  .guide { stroke: var(--guide); stroke-width: 1; stroke-dasharray: 14 10; fill: none; }
  .band { fill: var(--peach); }
  .ribbon { fill: var(--peach); }
  .ribbon-stitch { fill: none; stroke: var(--paper); stroke-width: 0.8; stroke-dasharray: 3 2; }
  .made-in { font-family: 'Josefin Sans', sans-serif; font-weight: 300; fill: var(--muted); }
  .made-in-light { font-family: 'Josefin Sans', sans-serif; font-weight: 300; fill: var(--paper); }
  .country { font-family: 'Nunito', sans-serif; font-weight: 900; font-style: italic; fill: var(--ink); }
  .country-light { font-family: 'Nunito', sans-serif; font-weight: 900; font-style: italic; fill: var(--paper); }
  .seal-ring { fill: var(--paper); stroke: var(--peach); stroke-width: 7; }
  .seal-pct { font-family: 'Nunito', sans-serif; font-weight: 900; font-style: italic; fill: var(--peach); }
  .seal-text { font-family: 'Josefin Sans', sans-serif; font-weight: 600; fill: var(--ink); }
  .pennant { fill: var(--ink); }
  .pennant-stitch { fill: none; stroke: var(--paper); stroke-width: 1; stroke-dasharray: 4 3; }
  .product-name { font-family: 'Oswald', sans-serif; font-weight: 500; fill: var(--paper); }
  .product-sub { font-family: 'Josefin Sans', sans-serif; font-weight: 300; fill: var(--paper); }
  .brand-name { font-family: 'Nunito', sans-serif; font-weight: 900; fill: var(--ink); }
  .descriptor { font-family: 'Josefin Sans', sans-serif; font-weight: 300; font-style: italic; fill: var(--paper); }
  .descriptor-dark { font-family: 'Josefin Sans', sans-serif; font-weight: 300; font-style: italic; fill: var(--ink); }
  .weight-badge { fill: var(--paper); stroke: var(--peach); stroke-width: 3; }
  .weight-num { font-family: 'Nunito', sans-serif; font-weight: 900; fill: var(--peach); }
  .weight-unit { font-family: 'Josefin Sans', sans-serif; font-weight: 400; fill: var(--ink); }
  .panel-title { font-family: 'Nunito', sans-serif; font-weight: 900; font-style: italic; fill: var(--paper); }
  .nip-frame { fill: var(--paper); stroke: var(--ink); stroke-width: 1.5; }
  .nip-grid { stroke: var(--ink); stroke-width: 0.6; fill: none; }
  .nip-cell { font-family: Arial, Helvetica, sans-serif; font-size: 7px; fill: var(--ink); }
  .lid-ring { fill: var(--peach); }
  .lid-stitch { fill: none; stroke: var(--paper); stroke-width: 2; stroke-dasharray: 2 3; }
</style>
</head>
<body>
<svg class="artboard" viewBox="0 0 1200 665" xmlns="http://www.w3.org/2000/svg">
  <defs>
    <linearGradient id="hide-light" x1="0" y1="0" x2="0" y2="1">
      <stop offset="0" stop-color="#ffffff"/>
      <stop offset="0.35" stop-color="#f6e5db"/>
      <stop offset="1" stop-color="#f3dccf"/>
    </linearGradient>
    <linearGradient id="hide-deep" x1="0" y1="0" x2="1" y2="0">
      <stop offset="0" stop-color="#e09c7b"/>
      <stop offset="0.5" stop-color="#e5a888"/>
      <stop offset="1" stop-color="#e09c7b"/>
    </linearGradient>
  </defs>

  <!-- side tags and guides -->
  <text class="side-tag" x="300" y="36" text-anchor="middle">FRONT</text>
  <text class="side-tag" x="898" y="36" text-anchor="middle">BACK</text>
  <line class="guide" x1="12" y1="41" x2="1200" y2="41"/>
  <line class="guide" x1="0" y1="381" x2="1200" y2="381"/>

  <!-- wrap label: front -->
  <g class="wrap-label">
    <rect x="0" y="61" width="898" height="307" fill="var(--paper)"/>
    <rect x="0" y="150" width="898" height="131" fill="url(#hide-light)" role="img" aria-label="Soft cow-hide spot pattern"/>
    <rect x="0" y="281" width="898" height="87" fill="url(#hide-deep)" role="img" aria-label="Cow-hide spot pattern in peach tones"/>
    <rect class="band" x="0" y="115" width="898" height="12"/>

    <!-- left ribbon -->
    <polygon class="ribbon" points="71,104 243,104 228,124.5 243,145 71,145 86,124.5"/>
    <polygon class="ribbon-stitch" points="80,108 234,108 222,124.5 234,141 80,141 92,124.5"/>
    <text class="made-in" x="157" y="122" font-size="12" text-anchor="middle">Made in</text>
    <text class="country" x="157" y="134" font-size="12.5" text-anchor="middle">Papua New Guinea.</text>

    <!-- right ribbon -->
    <polygon class="ribbon" points="711,104 883,104 868,124.5 883,145 711,145 726,124.5"/>
    <polygon class="ribbon-stitch" points="720,108 874,108 862,124.5 874,141 720,141 732,124.5"/>
    <text class="made-in" x="797" y="122" font-size="12" text-anchor="middle">Made in</text>
    <text class="country" x="797" y="134" font-size="12.5" text-anchor="middle">Papua New Guinea.</text>

    <!-- natural seal -->
    <circle class="seal-ring" cx="412" cy="95" r="69"/>
    <text class="seal-pct" x="412" y="96" font-size="27" text-anchor="middle">100%</text>
    <text class="seal-text" x="412" y="115" font-size="19" text-anchor="middle">NATURAL</text>
    <text class="seal-text" x="412" y="134" font-size="19" text-anchor="middle">PRODUCT</text>

    <!-- product pennant -->
    <path class="pennant" d="M547,50 H653 V190 L600,160 L547,190 Z"/>
    <path class="pennant-stitch" d="M556,62 H644 V177 L600,154 L556,177 Z"/>
    <text class="product-name" x="600" y="124" font-size="52" text-anchor="middle">BEEF</text>
    <text class="product-sub" x="600" y="148" font-size="20" text-anchor="middle">TALLOW</text>

    <!-- brand -->
    <text class="brand-name" x="600" y="232" font-size="19" text-anchor="middle">Telby Preserving Co</text>
    <text class="brand-name" x="157" y="245" font-size="12" text-anchor="middle">Telby Preserving Co</text>

    <!-- descriptors -->
    <text class="descriptor" x="157" y="304" font-size="15" text-anchor="middle">Suet, Tallow, Beef Fat</text>
    <text class="descriptor" x="600" y="325" font-size="23" text-anchor="middle">Suet, Tallow, Beef Fat</text>

    <!-- net weight -->
    <circle class="weight-badge" cx="813" cy="296" r="37"/>
    <text class="weight-num" x="813" y="300" font-size="27" text-anchor="middle">500</text>
    <text class="weight-unit" x="813" y="317" font-size="21" text-anchor="middle">gm</text>
    <circle cx="35" cy="314" r="21" fill="var(--paper)"/>
    <text class="weight-num" x="35" y="316" font-size="14" text-anchor="middle">500</text>
    <text class="weight-unit" x="35" y="327" font-size="11" text-anchor="middle">gm</text>
  </g>

  <!-- wrap label: back -->
  <g class="back-panel">
    <rect x="898" y="55" width="302" height="313" fill="url(#hide-deep)" role="img" aria-label="Cow-hide spot pattern in peach tones"/>
    <rect x="898" y="78" width="302" height="19" fill="var(--paper)"/>
    <text class="descriptor-dark" x="1054" y="93" font-size="15" text-anchor="middle">Suet, Tallow, Beef Fat</text>
    <text class="panel-title" x="1054" y="132" font-size="18" text-anchor="middle">Nutrition Facts</text>

    <rect class="nip-frame" x="981" y="139" width="147" height="61"/>
    <g class="nip-grid">
      <rect x="986" y="151" width="137" height="44"/>
      <line x1="986" y1="163" x2="1123" y2="163"/>
      <line x1="986" y1="173" x2="1123" y2="173"/>
      <line x1="986" y1="184" x2="1123" y2="184"/>
      <line x1="1021" y1="151" x2="1021" y2="195"/>
      <line x1="1055" y1="151" x2="1055" y2="195"/>
      <line x1="1089" y1="151" x2="1089" y2="195"/>
    </g>
    <text class="nip-cell" x="1022" y="160">weight</text>
    <text class="nip-cell" x="1056" y="160">AUD</text>
    <text class="nip-cell" x="1090" y="160">PGK</text>
    <text class="nip-cell" x="987" y="171">Tub/Pail</text>
    <text class="nip-cell" x="1022" y="171">500gm</text>
    <text class="nip-cell" x="1088" y="171" text-anchor="end">0,927</text>
    <text class="nip-cell" x="1122" y="171" text-anchor="end">2,4102</text>
    <text class="nip-cell" x="987" y="181">Lid</text>
    <text class="nip-cell" x="1088" y="181" text-anchor="end">0,236</text>
    <text class="nip-cell" x="1122" y="181" text-anchor="end">0,6136</text>
    <text class="nip-cell" x="987" y="192">Total</text>
    <text class="nip-cell" x="1122" y="192" text-anchor="end">3,02</text>

    <text class="made-in-light" x="1048" y="272" font-size="12" text-anchor="middle">Made in</text>
    <text class="country-light" x="1050" y="283" font-size="12.5" text-anchor="middle">Papua New Guinea.</text>
    <text class="brand-name" x="1054" y="314" font-size="12" text-anchor="middle">Telby Preserving Co</text>
  </g>

  <!-- lid label -->
  <g class="lid-label">
    <polygon class="ribbon" points="354,501 530,501 530,542 354,542 372,521.5"/>
    <polygon class="ribbon-stitch" points="364,505 525,505 525,538 364,538 379,521.5"/>
    <polygon class="ribbon" points="670,501 846,501 828,521.5 846,542 670,542"/>
    <polygon class="ribbon-stitch" points="675,505 836,505 821,521.5 836,538 675,538"/>
    <circle class="lid-ring" cx="600" cy="521" r="100"/>
    <circle class="lid-stitch" cx="600" cy="521" r="89"/>
    <circle cx="600" cy="521" r="74" fill="var(--paper)"/>
    <text class="made-in" x="438" y="519" font-size="12" text-anchor="middle">Made in</text>
    <text class="country" x="440" y="531" font-size="12.5" text-anchor="middle">Papua New Guinea.</text>
    <text class="made-in" x="758" y="519" font-size="12" text-anchor="middle">Made in</text>
    <text class="country" x="760" y="531" font-size="12.5" text-anchor="middle">Papua New Guinea.</text>

    <path class="pennant" d="M558,416 H640 V527 L600,503 L558,527 Z"/>
    <path class="pennant-stitch" d="M566,426 H632 V515 L600,497 L566,515 Z"/>
    <text class="product-name" x="599" y="476" font-size="40" text-anchor="middle">BEEF</text>
    <text class="product-sub" x="599" y="494" font-size="15" text-anchor="middle">TALLOW</text>
    <text class="brand-name" x="600" y="558" font-size="13" text-anchor="middle">Telby Preserving Co</text>
  </g>
</svg>
</body>
</html>
```